International Hand & Body company needing a Hand cream tube design for the Retail market

I am wanting a modern design for a new range of 6 hand creams I will be launching in August. They need to compliment our range of wrapped soaps which you can see on www.plomvane.com.au so am wanting clean designs. I am wanting a solid colour with a hand drawn organic feel line drawing in black elegantly placed wrapping around the label. I am wanting to focus on the colour and positioning of words and fonts. I like modern clean contemporary fonts. The final design needs to appeal to the broader female market.This may lead to range expansion if designs are well received.
Updates

These designs are not hitting the brief. They are too generic and look like a supermarket brand. Our brand is more boutique and this design needs to be modern and simple. I would like more solid colours and more modern designs. Without patterns.

Target Market(s)

Female aged 20 - 70

Requirements
Must have
• a modern contemporary design that will appeal to the masses.
• Please read attached brief.
Should not have
• a black botanical illustration, in a loose and organic design to match the fragrance.

```html
<!DOCTYPE html>
<html lang="en">
<head>
<meta charset="utf-8">
<title>plomvane — hand cream label presentation</title>
<link rel="stylesheet" href="https://fonts.googleapis.com/css2?family=Open+Sans:wght@400;700&family=Raleway:wght@200&family=Advent+Pro:wght@400&display=swap">
<style>
  :root {
    --sand: #efdfcd;
    --teal: #69c9cf;
    --sky: #dcf0f7;
    --gold-dark: #c39a52;
    --gold-light: #f2e2b6;
    --ink: #1f1f1f;
    --mist: #9a9fa2;
    --wood-light: #f3d9b8;
    --wood-dark: #e2b88a;
  }
  * { margin: 0; padding: 0; box-sizing: border-box; }
  html, body { width: 1200px; height: 960px; overflow: hidden; background: var(--sand); }
  .board { position: relative; width: 1200px; height: 960px; background: var(--sand); font-family: "Open Sans", sans-serif; }
  .header-bands { position: absolute; left: 0; top: 0; }
  .brand-title {
    position: absolute; left: 0; width: 1200px; top: 150px; text-align: center;
    font-family: "Open Sans", sans-serif; font-weight: 400; font-size: 80px;
    letter-spacing: 0.22em; color: var(--ink); line-height: 1; padding-left: 90px;
    white-space: nowrap;
  }
  .label { position: absolute; left: 123px; top: 314px; width: 400px; height: 590px; }
  .label-panel { position: absolute; top: 0; height: 590px; width: 200px; }
  .panel-front { left: 0; }
  .panel-back { left: 200px; }
  .label-sky { position: absolute; left: 0; top: 0; width: 400px; height: 256px; background: var(--sky); }
  .label-gold { position: absolute; left: 0; top: 256px; width: 400px; height: 22px;
    background: linear-gradient(90deg, var(--gold-dark), var(--gold-light) 55%, var(--gold-dark)); }
  .label-teal { position: absolute; left: 0; top: 278px; width: 400px; height: 312px; background: var(--teal); }
  .fold-line { position: absolute; left: 322px; top: 255px; width: 1px; height: 691px; background: var(--ink); }
  .label-name { position: absolute; font-weight: 400; color: var(--ink); line-height: 1; white-space: nowrap; }
  .front-name { left: 31px; top: 222px; font-size: 24px; letter-spacing: 0.1em; }
  .back-name { right: 14px; top: 40px; font-size: 26px; letter-spacing: 0.1em; }
  .condensed { transform: scaleX(0.82); transform-origin: left center; white-space: nowrap; }
  .scent { position: absolute; left: 31px; top: 290px; font-family: "Advent Pro", sans-serif;
    font-size: 16px; letter-spacing: 0.1em; color: var(--ink); }
  .product-type { position: absolute; left: 52px; top: 508px; font-family: "Advent Pro", sans-serif; font-size: 8px; letter-spacing: 0.1em; color: var(--ink); }
  .origin { position: absolute; left: 36px; top: 522px; font-family: "Advent Pro", sans-serif; font-size: 10px; letter-spacing: 0.12em; color: var(--ink); }
  .volume { position: absolute; left: 66px; top: 536px; font-size: 5px; color: #4a6f73; white-space: nowrap; }
  .tagline { position: absolute; right: 18px; top: 100px; width: 170px; text-align: right;
    font-family: "Raleway", sans-serif; font-weight: 200; font-size: 16px; line-height: 21px; color: var(--mist); }
  .ingredients { position: absolute; left: 80px; top: 290px; width: 108px; font-size: 6px; line-height: 8.8px;
    text-align: justify; color: var(--ink); font-weight: 400; }
  .ingredients strong { font-weight: 700; }
  .product-photo { position: absolute; left: 660px; top: 421px; width: 390px; height: 390px;
    background: linear-gradient(160deg, var(--wood-light), var(--wood-dark)); box-shadow: 6px 10px 18px rgba(120,90,60,0.25); }
</style>
</head>
<body>
<main class="board">
  <svg class="header-bands" width="1200" height="180" viewBox="0 0 1200 180" aria-hidden="true">
    <defs>
      <linearGradient id="goldSweep" x1="0" x2="1" y1="0" y2="0">
        <stop offset="0" stop-color="#c39a52"/>
        <stop offset="0.5" stop-color="#f2e2b6"/>
        <stop offset="1" stop-color="#c39a52"/>
      </linearGradient>
    </defs>
    <polygon points="0,52 610,146 1200,52 1200,64 610,172 0,64" fill="url(#goldSweep)"/>
    <polygon points="0,0 610,0 610,146 0,52" fill="#69c9cf"/>
    <polygon points="610,0 1200,0 1200,52 610,146" fill="#dcf0f7"/>
  </svg>

  <h1 class="brand-title">plomvane</h1>

  <section class="label" aria-label="Hand cream label layout">
    <div class="label-sky"></div>
    <div class="label-gold"></div>
    <div class="label-teal"></div>

    <div class="label-panel panel-front">
      <p class="label-name front-name">plomvane</p>
      <p class="scent condensed">CITRUS E EAGRASS</p>
      <p class="product-type condensed">HAND CREAM</p>
      <p class="origin condensed">MADE IN AUSTRALIA</p>
      <p class="volume">35 mL &nbsp;&nbsp; 1.18 fl.oz</p>
    </div>

    <div class="label-panel panel-back">
      <p class="label-name back-name">plomvane</p>
      <p class="tagline">A nourishing<br>non-greasy hand<br>cream to kep skin<br>soft &amp; hydrated.</p>
      <p class="ingredients"><strong>INGREDIENTS:</strong> AQUA, HELANTHUS ANNUUS SEED OIL, STEARIC ACID, GLYCERIN, CETEARYL ALCOHOL, CERA ALBA, GLYCERYL STEARATE, DIMETHICONE, PRUNUS AMYGDALUS DULCIS OIL ALMOND OIL, PAFUM, PHENOXYETHANOL, TRIETHANOLAMINE, TOCOPHERYL ACETATE, CAPRYLYL GLYCOL, SODUIM PCA, DISODIUM EDTA, ALOE BARBADENSIS LEAF JUICE POWDER (ALOE VERA), DECYLENE GLYCOL, THEOBROMA CACAO SEED BUTTER (COCOA), COCOS NUCIFERA (COCONUT) OIL, BUTYROSPERMUM PARKII (SHEA) BUTTER</p>
    </div>
  </section>
  <div class="fold-line"></div>

  <div class="product-photo" role="img" aria-label="Product photograph: boxed hand cream and tube on a light wooden board"></div>
</main>
</body>
</html>
```